Book cover for The Quiet Lioness Manual to Turn into a Powerhouse at Work

Book cover design for soft cover non-fiction book.

The front cover is what is most important at this stage, I am still gathering the testimonials and book description for the back cover so a rough to be completed later for the back is great.

Title as per above. Divided up "The Quiet Lioness Manual" (to be a series) and "Turn into a Powerhouse at Work" in this book in the series

Also for the front:

Lorna Kevesh

"The most unusual business book you will read." - Gwen Talrowicz, Author of Founder Sunrise

Background info:

This work is a blending of the masculine and feminine energies, the practical business skills with a strong focus on the inner game. I am looking for the cover to have a nod to the Dominatrix and a clear message that one can be soft (kind, open hearted) and still be strong and firm in business.

Photo options are in this file https://www.filecrate-example.net/sh/qmx41tgbw8vkrle/BBEtmkqpQ2XrLm3nXoyy94J4b?dl=0

Size 6" x 9" 179 pgs

Target Market(s)

female entreprenures

Industry/Entity Type

Business

Colors

Designer to choose colors to be used in the design.

Requirements
Must have
• I would like the title to be in a font that is bold and upscale, to contrast the softness fo the image.
• Clear and readable
• Unique look that will stand out
Should not have
• overt Dominatrix images or slant. It is about the energy not the actual.

```html
<!DOCTYPE html>
<html lang="en">
<head>
<meta charset="utf-8">
<title>The Quiet Lioness Manual – Book Cover</title>
<link rel="stylesheet" href="https://fonts.googleapis.com/css2?family=Cinzel:wght@700;900&family=Tinos:wght@400&display=swap">
<style>
  :root {
    --stage: #1b1b1d;
    --ink: #050507;
    --paper: #ffffff;
    --royal: #2340c2;
    --quote-blue: #3d56d6;
    --sky-light: #e3f4f8;
    --sky-mid: #a6d6e4;
    --sky-deep: #7fc3d8;
    --warm-light: #e6d6bf;
    --warm-mid: #c9a98c;
    --teal: #1f8fb5;
    --teal-deep: #14708f;
    --title-font: "Cinzel", serif;
    --body-font: "Tinos", serif;
  }
  * { box-sizing: border-box; margin: 0; padding: 0; }
  html, body {
    width: 1200px;
    height: 600px;
    overflow: hidden;
    background: var(--stage);
  }
  .canvas {
    position: relative;
    width: 1200px;
    height: 600px;
    display: flex;
    justify-content: center;
  }
  .cover {
    position: relative;
    width: 400px;
    height: 600px;
    background: var(--ink);
    overflow: hidden;
  }
  .pattern-field {
    position: absolute;
    left: 0;
    top: 0;
    width: 400px;
    height: 360px;
    background: linear-gradient(150deg, var(--sky-light) 0%, var(--sky-mid) 55%, var(--sky-deep) 100%);
  }
  .portrait {
    position: absolute;
    left: 138px;
    top: 16px;
    width: 254px;
    height: 344px;
    background: linear-gradient(180deg,
      var(--warm-light) 0%,
      var(--warm-mid) 38%,
      var(--teal) 58%,
      var(--teal-deep) 100%);
  }
  .title-block {
    position: absolute;
    left: 0;
    top: 266px;
    width: 286px;
    height: 160px;
    background: var(--royal);
    padding: 8px 0 0 36px;
  }
  .series-title {
    font-family: var(--title-font);
    font-weight: 900;
    font-size: 29px;
    line-height: 41px;
    color: var(--ink);
    letter-spacing: 0.3px;
    text-transform: uppercase;
  }
  .series-name {
    margin-top: 2px;
    font-family: var(--body-font);
    font-size: 16px;
    color: var(--paper);
  }
  .endorsement {
    position: absolute;
    left: 29px;
    top: 442px;
    font-family: var(--body-font);
  }
  .endorsement-quote {
    font-size: 13px;
    color: var(--quote-blue);
  }
  .endorsement-source {
    margin-top: 5px;
    margin-left: 6px;
    font-size: 10px;
    color: var(--paper);
  }
  .endorsement-credit {
    font-size: 7.5px;
    margin-left: 4px;
  }
  .author-rule {
    position: absolute;
    left: 34px;
    top: 507px;
    width: 314px;
    height: 2.5px;
    background: var(--paper);
  }
  .author-name {
    position: absolute;
    left: 33px;
    top: 516px;
    font-family: var(--title-font);
    font-weight: 900;
    font-size: 35px;
    line-height: 1.1;
    color: var(--paper);
    letter-spacing: 0.3px;
    text-transform: uppercase;
    white-space: nowrap;
  }
  .frame {
    position: absolute;
    left: 18px;
    top: 18px;
    width: 362px;
    height: 556px;
    border: 2.5px solid var(--paper);
    pointer-events: none;
  }
</style>
</head>
<body>
  <main class="canvas">
    <article class="cover">
      <div class="pattern-field" role="img" aria-label="Pale blue swirling line pattern filling the upper cover"></div>
      <div class="portrait" role="img" aria-label="Portrait photo of the author with short blonde hair in a teal top, hand resting at her neck"></div>

      <section class="title-block">
        <h1 class="series-title">Turn into a<br>Powerhouse<br>at Work</h1>
        <p class="series-name">The Quiet Lioness Manual</p>
      </section>

      <blockquote class="endorsement">
        <p class="endorsement-quote">"The most unusual business book you will read."</p>
        <p class="endorsement-source">Gwen Talrowicz <span class="endorsement-credit">Author of Founder Sunrise</span></p>
      </blockquote>

      <div class="author-rule"></div>
      <p class="author-name">Lorna Kevesh</p>

      <div class="frame"></div>
    </article>
  </main>
</body>
</html>
```